Health software company called BRIGHT HARBOR, committed to innovation and technological excellence

The powerpoint presentation template is necessary, very necessary is elegant and modern with innovative images and the color palette attached. The presentation will be used for the business plan and investor presentations that we will use to raise funds. Please, recommend a modern typeface, as well as format to be able to use it and incorporate it as part of the company's brand guidelines. Great diversity of technological solutions

Very low attendance of designers for a high budget. Very few proposals and no capture my interest

Target Market(s)

managers, managers of public and private health centers, government states, investors

Industry/Entity Type

It Company

Font styles to use
Serif

Requirements
Must have
• The powerpoint presentation template is necessary, very necessary is elegant, minimalist and modern with innovative images and the color palette attached. it must be refined in demarcated style
Nice to have
• very nice, visually harmonic avoid saturation
Should not have
• NO dark colors NO dark colors NO dark colors NO dark colors NO dark colors

```html
<!DOCTYPE html>
<html lang="en">
<head>
<meta charset="utf-8">
<title>BRIGHT HARBOR – Presentation Template</title>
<link href="https://fonts.googleapis.com/css2?family=Cormorant+Garamond:wght@500;600&family=Lora:wght@400;600&display=swap" rel="stylesheet">
<style>
:root{
  --page:#eef1f5;
  --slide:#fbfcfe;
  --footer:#e7edf4;
  --title:#1f2a3c;
  --body:#4c5668;
  --muted:#6b7587;
  --accent:#1b9ce0;
  --accent-deep:#1483cc;
  --card:#edf1f6;
  --card-line:#dbe3ec;
  --photo-a:#c9d6e3;
  --photo-b:#e8eef5;
}
*{box-sizing:border-box;margin:0;padding:0}
html,body{width:1200px;height:1200px;overflow:hidden;background:var(--page);font-family:"Lora",serif}
.slide{position:absolute;background:var(--slide);overflow:hidden;color:var(--title);box-shadow:0 1px 4px rgba(31,42,60,.08)}
.slide-footer{position:absolute;left:0;right:0;bottom:0;height:42px;background:var(--footer)}
.brand{position:absolute;left:32px;bottom:9px;display:flex;align-items:center;gap:6px}
.brand-dot{width:22px;height:22px;border-radius:50%;border:4px solid var(--accent)}
.brand-name{font-size:7px;font-weight:600;letter-spacing:.8px;line-height:1.15;color:var(--title);width:44px}
.page-no{position:absolute;right:32px;bottom:17px;font-size:7px;color:var(--muted)}
.title{position:absolute;font-family:"Cormorant Garamond",serif;font-weight:500;font-size:29px;line-height:1.1;color:var(--title)}
.body-text{position:absolute;font-size:6.2px;line-height:2.05;color:var(--body)}
.photo{position:absolute;background:linear-gradient(135deg,var(--photo-b),var(--photo-a))}
.service-head{position:absolute;font-size:9.5px;color:var(--accent);display:flex;align-items:center;gap:8px;white-space:nowrap}
.service-head b{font-weight:600}
.icon{width:16px;height:16px;fill:none;stroke:var(--accent);stroke-width:1.6;stroke-linecap:round;stroke-linejoin:round}
.subtitle{position:absolute;font-size:5.5px;letter-spacing:1px;color:var(--accent);font-weight:600}
.card{position:absolute;top:105px;width:155px;height:152px;background:var(--card);border:1px solid var(--card-line);text-align:center}
.card.is-active{background:linear-gradient(180deg,var(--accent),var(--accent-deep));border-color:var(--accent-deep)}
.card .icon{position:absolute;left:59px;top:24px;width:36px;height:36px;stroke-width:1.3}
.card.is-active .icon{stroke:#ffffff}
.card-head{position:absolute;left:0;right:0;top:79px;font-size:9.5px;color:var(--accent)}
.card.is-active .card-head{color:#ffffff}
.card-body{position:absolute;left:20px;right:20px;top:98px;font-size:6px;line-height:2.1;color:var(--body)}
.card.is-active .card-body{color:#eaf5fd}
</style>
</head>
<body>

<!-- Slide 2 -->
<section class="slide" style="left:21px;top:78px;width:572px;height:322px">
  <h2 class="title" style="left:41px;top:54px">Demo slide<br>With text</h2>
  <p class="body-text" style="left:41px;top:134px;width:226px">Lorem ipsum dolor sit amet, consectetur adipiscing elit, sed do eiusmod tempor incididunt ut labore et dolore magna aliqua. Ut enim ad minim veniam, quis nostrud exercitation ullamco laboris nisi ut aliquip ex ea commodo consequat. Duis aute irure dolor in reprehenderit in voluptate velit esse cillum dolore eu fugiat nulla pariatur. Excepteur sint occaecat cupidatat non proident, sunt in culpa qui officia deserunt voluptatem accusantium doloremque</p>
  <div class="photo" role="img" aria-label="Business team meeting around a table with laptops" style="left:286px;top:22px;width:286px;height:232px"></div>
  <div class="slide-footer"></div>
  <div class="brand"><span class="brand-dot"></span><span class="brand-name">BRIGHT HARBOR</span></div>
  <span class="page-no">2</span>
</section>

<!-- Slide 3 -->
<section class="slide" style="left:606px;top:78px;width:572px;height:322px">
  <h2 class="title" style="left:41px;top:54px">Demo slide<br>With text</h2>
  <p class="body-text" style="left:41px;top:134px;width:226px">Lorem ipsum dolor sit amet, consectetur adipiscing elit, sed do eiusmod tempor incididunt ut labore et dolore magna aliqua. Ut enim ad minim veniam, quis nostrud exercitation ullamco laboris nisi ut aliquip ex ea commodo consequat. Duis aute irure dolor in reprehenderit in voluptate velit esse cillum dolore eu fugiat nulla pariatur. Excepteur sint occaecat cupidatat non proident, sunt in culpa qui officia deserunt voluptatem accusantium doloremque</p>
  <p class="body-text" style="left:306px;top:134px;width:226px">Lorem ipsum dolor sit amet, consectetur adipiscing elit, sed do eiusmod tempor incididunt ut labore et dolore magna aliqua. Ut enim ad minim veniam, quis nostrud exercitation ullamco laboris nisi ut aliquip ex ea commodo consequat. Duis aute irure dolor in reprehenderit in voluptate velit esse cillum dolore eu fugiat nulla pariatur. Excepteur sint occaecat cupidatat non proident, sunt in culpa qui officia deserunt voluptatem accusantium doloremque</p>
  <div class="slide-footer"></div>
  <div class="brand"><span class="brand-dot"></span><span class="brand-name">BRIGHT HARBOR</span></div>
  <span class="page-no">3</span>
</section>

<!-- Slide 4: Agenda -->
<section class="slide" style="left:16px;top:434px;width:577px;height:324px">
  <span class="subtitle" style="left:38px;top:42px">SUBTITLE TEXT</span>
  <h2 class="title" style="left:37px;top:54px;font-size:30px">Presentation Agenda</h2>
  <div class="photo" role="img" aria-label="Confident businessman in front of colleagues talking in an office" style="left:14px;top:90px;width:266px;height:177px"></div>
  <div class="service-head" style="left:338px;top:42px"><span><b>01.</b> Text about service</span></div>
  <p class="body-text" style="left:338px;top:60px;width:205px">Lorem ipsum dolor sit amet, consectetur adipiscing elit, sed do eiusmod tempor incididunt ut labore et dolore</p>
  <div class="service-head" style="left:338px;top:109px"><span><b>02.</b> Text about service</span></div>
  <p class="body-text" style="left:338px;top:127px;width:205px">Lorem ipsum dolor sit amet, consectetur adipiscing elit, sed do eiusmod tempor incididunt ut labore et dolore</p>
  <div class="service-head" style="left:338px;top:176px"><span><b>03.</b> Text about service</span></div>
  <p class="body-text" style="left:338px;top:194px;width:205px">Lorem ipsum dolor sit amet, consectetur adipiscing elit, sed do eiusmod tempor incididunt ut labore et dolore</p>
  <div class="slide-footer"></div>
  <div class="brand"><span class="brand-dot"></span><span class="brand-name">BRIGHT HARBOR</span></div>
  <span class="page-no">4</span>
</section>

<!-- Slide 5: Services -->
<section class="slide" style="left:606px;top:436px;width:570px;height:321px">
  <h2 class="title" style="left:41px;top:38px">Our Services</h2>
  <div class="service-head" style="left:41px;top:97px">
    <svg class="icon" viewBox="0 0 16 16"><path d="M4 2h8v4a4 4 0 0 1-8 0z M4 3H2v1a2 2 0 0 0 2 2 M12 3h2v1a2 2 0 0 1-2 2 M8 10v3 M5 14h6"/></svg>
    <span>Text about service</span></div>
  <p class="body-text" style="left:65px;top:116px;width:205px">Lorem ipsum dolor sit amet, consectetur adipiscing elit, sed do eiusmod tempor incididunt ut labore et dolore magna aliqua. Ut enim ad minim veniam, quis nostrud</p>
  <div class="service-head" style="left:304px;top:97px">
    <svg class="icon" viewBox="0 0 16 16"><path d="M14 2c-4 0-7 2-9 6l3 3c4-2 6-5 6-9z M5 8H2l2-3h3 M8 11v3l3-2V9 M4 12l-2 2"/></svg>
    <span>Text about service</span></div>
  <p class="body-text" style="left:329px;top:116px;width:205px">Lorem ipsum dolor sit amet, consectetur adipiscing elit, sed do eiusmod tempor incididunt ut labore et dolore magna aliqua. Ut enim ad minim veniam, quis nostrud</p>
  <div class="service-head" style="left:41px;top:180px">
    <svg class="icon" viewBox="0 0 16 16"><circle cx="8" cy="3" r="1.8"/><path d="M5 15V7h6v8 M8 9v6"/></svg>
    <span>Text about service</span></div>
  <p class="body-text" style="left:65px;top:199px;width:205px">Lorem ipsum dolor sit amet, consectetur adipiscing elit, sed do eiusmod tempor incididunt ut labore et dolore magna aliqua. Ut enim ad minim veniam, quis nostrud</p>
  <div class="service-head" style="left:304px;top:180px">
    <svg class="icon" viewBox="0 0 16 16"><circle cx="8" cy="8" r="6"/><circle cx="8" cy="8" r="3.2"/><circle cx="8" cy="8" r=".8"/></svg>
    <span>Text about service</span></div>
  <p class="body-text" style="left:329px;top:199px;width:205px">Lorem ipsum dolor sit amet, consectetur adipiscing elit, sed do eiusmod tempor incididunt ut labore et dolore magna aliqua. Ut enim ad minim veniam, quis nostrud</p>
  <div class="slide-footer"></div>
  <div class="brand"><span class="brand-dot"></span><span class="brand-name">BRIGHT HARBOR</span></div>
  <span class="page-no">5</span>
</section>

<!-- Slide 6: Team -->
<section class="slide" style="left:18px;top:808px;width:574px;height:324px">
  <div class="photo" role="img" aria-label="Businesswoman holding documents with colleagues behind her" style="left:45px;top:47px;width:142px;height:111px"></div>
  <div class="photo" role="img" aria-label="Smiling businessman shaking hands" style="left:218px;top:47px;width:142px;height:111px"></div>
  <div class="photo" role="img" aria-label="Smiling professional seated in an office with coworkers" style="left:390px;top:47px;width:142px;height:111px"></div>
  <div class="service-head" style="left:44px;top:186px">
    <svg class="icon" viewBox="0 0 16 16"><path d="M4 2h8v4a4 4 0 0 1-8 0z M4 3H2v1a2 2 0 0 0 2 2 M12 3h2v1a2 2 0 0 1-2 2 M8 10v3 M5 14h6"/></svg>
    <span>Text about service</span></div>
  <p class="body-text" style="left:68px;top:205px;width:122px">Lorem ipsum dolor sit amet, consectetur adipiscing elit, sed do labore et dolore magna aliqua Ut</p>
  <div class="service-head" style="left:217px;top:186px">
    <svg class="icon" viewBox="0 0 16 16"><path d="M4 3h8l3 4-7 7-7-7z M1 7h14 M6 3l2 11 2-11"/></svg>
    <span>Text about service</span></div>
  <p class="body-text" style="left:241px;top:205px;width:122px">Lorem ipsum dolor sit amet, consectetur adipiscing elit, sed do labore et dolore magna aliqua Ut</p>
  <div class="service-head" style="left:390px;top:186px">
    <svg class="icon" viewBox="0 0 16 16"><path d="M14 2c-4 0-7 2-9 6l3 3c4-2 6-5 6-9z M5 8H2l2-3h3 M8 11v3l3-2V9 M4 12l-2 2"/></svg>
    <span>Text about service</span></div>
  <p class="body-text" style="left:414px;top:205px;width:122px">Lorem ipsum dolor sit amet, consectetur adipiscing elit, sed do labore et dolore magna aliqua Ut</p>
  <div class="slide-footer"></div>
  <div class="brand"><span class="brand-dot"></span><span class="brand-name">BRIGHT HARBOR</span></div>
  <span class="page-no">6</span>
</section>

<!-- Slide 7: Infographic -->
<section class="slide" style="left:601px;top:806px;width:576px;height:326px">
  <h2 class="title" style="left:0;right:0;top:24px;text-align:center;font-size:30px">Demo slide<br>Infographic block</h2>
  <div class="card" style="left:42px">
    <svg class="icon" viewBox="0 0 36 36"><rect x="12" y="7" width="20" height="14"/><path d="M16 17l4-4 3 3 5-5 M5 30V20h6v10 M8 12a2.5 2.5 0 1 1 0 .1 M16 21v9 M28 21v9"/></svg>
    <div class="card-head">Text about service</div>
    <p class="card-body">Lorem ipsum dolor sit amet, consectetur adipiscing elit, sed do labore et dolore magna aliqua Ut</p>
  </div>
  <div class="card is-active" style="left:210px">
    <svg class="icon" viewBox="0 0 36 36"><rect x="4" y="10" width="28" height="20" rx="2"/><path d="M13 10V6h10v4 M4 18h28 M16 16h4v4h-4z"/></svg>
    <div class="card-head">Text about service</div>
    <p class="card-body">Lorem ipsum dolor sit amet, consectetur adipiscing elit, sed do labore et dolore magna aliqua Ut</p>
  </div>
  <div class="card" style="left:378px">
    <svg class="icon" viewBox="0 0 36 36"><path d="M6 31h26 M8 31v-7h5v7 M16 31V18h5v13 M24 31V12h5v19 M7 20l8-7 5 3 10-10 M26 6h4v4"/></svg>
    <div class="card-head">Text about service</div>
    <p class="card-body">Lorem ipsum dolor sit amet, consectetur adipiscing elit, sed do labore et dolore magna aliqua Ut</p>
  </div>
  <div class="slide-footer"></div>
  <div class="brand"><span class="brand-dot"></span><span class="brand-name">BRIGHT HARBOR</span></div>
  <span class="page-no">7</span>
</section>

</body>
</html>
```